Tincture bottle labels

I need my labels slightly adjusted to replace the ingredients part with the supplement facts as shown in the 3 Fernhollow labels attached, for the other 2 it will have to be copied and add an BQC disclosure on the label as well possibly below the storage info near the bottom of the label

Target Market(s)

Everyone

Industry/Entity Type

Vitamins & Supplements

Requirements
Must have
• Supplement facts box and info for each product and BQC disclosures

```html
<!DOCTYPE html>
<html lang="en">
<head>
<meta charset="utf-8">
<title>Fernhollow Cordyceps Liquid Drops Label</title>
<link href="https://fonts.googleapis.com/css2?family=Jost:ital,wght@0,400;0,500;0,700;1,700;1,800&family=Luckiest+Guy&family=Montserrat:wght@800&display=swap" rel="stylesheet">
<style>
  :root {
    --page: #f2f2f4;
    --purple-deep: #4b3a9c;
    --purple-mid: #6a3a9e;
    --purple-glow: #8a3aa6;
    --photo-dark: #6b4a1c;
    --photo-orange: #e08a2a;
    --photo-light: #f4b860;
    --brick: #9c4128;
    --brick-dark: #7a2f1c;
    --sky-blue: #1e9bd7;
    --ink: #111111;
    --white: #ffffff;
    --cap-red: #d7262e;
  }
  * { box-sizing: border-box; margin: 0; padding: 0; }
  html, body {
    width: 1200px; height: 814px; overflow: hidden;
    background: var(--page);
    font-family: "Jost", sans-serif;
  }
  .label {
    position: absolute; left: 91px; top: 214px;
    width: 1019px; height: 385px; overflow: hidden;
  }
  .label-bg { position: absolute; inset: 0; }
  .brick-band {
    position: absolute; left: 0; right: 0; top: 305px; bottom: 0;
    background: linear-gradient(180deg, var(--brick) 0%, var(--brick-dark) 100%);
    border-top: 4px solid var(--sky-blue);
  }
  .maker-info {
    position: absolute; left: 22px; top: 42px;
    transform-origin: left top; transform: rotate(90deg) translate(0, -56px);
    color: var(--white); font-size: 9.5px; line-height: 1.25; white-space: nowrap;
    display: flex; gap: 26px;
  }
  .maker-info strong { font-weight: 700; text-transform: uppercase; display: block; }
  .panel {
    position: absolute; background: var(--white);
    border: 3px solid var(--ink); border-radius: 16px;
    box-shadow: 6px 5px 0 var(--ink);
  }
  .facts-panel { left: 91px; top: 37px; width: 167px; height: 292px; padding: 10px 11px; }
  .facts-box { border: 1.5px solid var(--ink); padding: 2px 4px 2px; color: var(--ink); }
  .facts-title { font-weight: 700; font-size: 13.5px; line-height: 1.05; }
  .facts-small { font-size: 8px; font-weight: 500; line-height: 1.35; }
  .facts-head {
    display: flex; justify-content: space-between; font-weight: 700; font-size: 9.5px;
    border-top: 3.5px solid var(--ink); border-bottom: 1px solid var(--ink);
    margin-top: 2px; padding: 1px 0;
  }
  .facts-item { font-size: 11px; line-height: 1.35; padding: 2px 0 3px; border-bottom: 3px solid var(--ink); }
  .facts-note { font-size: 8px; padding-top: 1px; }
  .panel-block { color: var(--ink); margin-top: 7px; font-size: 10.5px; line-height: 1.2; }
  .panel-block h3 { font-family: "Luckiest Guy", sans-serif; font-weight: 400; font-size: 9px; letter-spacing: .2px; }
  .disclaimer {
    position: absolute; left: 57px; top: 338px; width: 240px; height: 38px;
    border: 1px solid var(--white); color: var(--white);
    font-size: 8.2px; line-height: 1.32; padding: 1px 4px;
  }
  .brand-name {
    position: absolute; left: 380px; width: 260px; top: 128px; text-align: center;
    font-family: "Luckiest Guy", sans-serif; font-size: 44px; color: var(--sky-blue);
  }
  .brand-dot {
    position: absolute; left: 490px; top: 58px; width: 42px; height: 42px;
    border-radius: 50%; background: var(--sky-blue);
  }
  .product-name {
    position: absolute; left: 380px; width: 260px; top: 218px; text-align: center;
    font-family: "Montserrat", sans-serif; font-weight: 800; font-size: 31px; letter-spacing: 1.5px;
    color: var(--white);
    text-shadow: -2px -2px 0 var(--ink), 2px -2px 0 var(--ink), -2px 2px 0 var(--ink), 2px 2px 0 var(--ink);
  }
  .format-pill {
    position: absolute; left: 417px; top: 280px; width: 186px; height: 47px;
    border-radius: 24px; background: var(--sky-blue); color: var(--white);
    display: flex; align-items: center; justify-content: center;
    font-size: 20px; font-weight: 400;
  }
  .volume {
    position: absolute; left: 380px; width: 260px; top: 339px; text-align: center;
    font-family: "Montserrat", sans-serif; font-weight: 800; font-size: 16px; letter-spacing: 1px; color: var(--white);
  }
  .mini-shroom {
    position: absolute; top: 268px; width: 34px; height: 38px;
    background: radial-gradient(circle at 50% 35%, var(--cap-red) 0 50%, transparent 52%),
                linear-gradient(var(--white), var(--white)) center 70% / 12px 16px no-repeat;
  }
  .benefits-panel { left: 775px; top: 37px; width: 181px; height: 288px; padding: 18px 12px 0 18px; }
  .benefits-headline {
    font-family: "Luckiest Guy", sans-serif; font-size: 19px; line-height: 1.3; text-align: center;
    color: var(--ink); letter-spacing: .3px;
  }
  .benefits-title { font-family: "Luckiest Guy", sans-serif; font-size: 17px; margin: 14px 0 0 14px; color: var(--ink); }
  .benefits-list { list-style: none; margin-top: 2px; }
  .benefits-list li {
    position: relative; padding-left: 14px; margin-bottom: 8px;
    font-style: italic; font-weight: 800; font-size: 15.5px; line-height: 1.03; color: var(--ink);
  }
  .benefits-list li::before {
    content: ""; position: absolute; left: 0; top: 50%; width: 5px; height: 5px;
    border-radius: 50%; background: var(--ink); transform: translateY(-50%);
  }
  .benefits-icon {
    position: absolute; left: 78px; bottom: 12px; width: 36px; height: 36px;
    border-radius: 50%; background: radial-gradient(circle at 50% 40%, var(--sky-blue) 0 55%, #cfe9f6 57%);
  }
</style>
</head>
<body>
  <main class="label">
    <svg class="label-bg" width="1019" height="385" viewBox="0 0 1019 385" aria-hidden="true">
      <defs>
        <linearGradient id="purpleFill" x1="0" y1="0" x2="0" y2="1">
          <stop offset="0" stop-color="var(--purple-deep)"/>
          <stop offset="0.7" stop-color="var(--purple-mid)"/>
          <stop offset="1" stop-color="var(--purple-glow)"/>
        </linearGradient>
      </defs>
      <rect width="1019" height="385" fill="url(#purpleFill)"/>
    </svg>
    <svg class="label-bg" width="1019" height="385" viewBox="0 0 1019 385" role="img" aria-label="Photograph of orange cordyceps militaris fruiting bodies">
      <defs>
        <linearGradient id="photoFill" x1="0" y1="0" x2="1" y2="1">
          <stop offset="0" stop-color="var(--photo-dark)"/>
          <stop offset="0.45" stop-color="var(--photo-orange)"/>
          <stop offset="1" stop-color="var(--photo-light)"/>
        </linearGradient>
      </defs>
      <path d="M0 0 H1019 V118 H490 C470 60 430 20 330 20 H0 Z" fill="url(#photoFill)"/>
    </svg>
    <div class="brick-band" role="img" aria-label="Red brick wall pattern"></div>

    <div class="maker-info">
      <p><strong>Manufactured by:</strong>Fernhollow LLC<br>Millbrook, Vermont</p>
      <p>fernhollow.shop</p>
    </div>

    <section class="panel facts-panel">
      <div class="facts-box">
        <h2 class="facts-title">Supplement Facts</h2>
        <p class="facts-small">Serving Size: 2 droppers (2ML)<br>Servings Per Container: About 30</p>
        <div class="facts-head"><span>Amount Per Serving</span><span>2mL*</span></div>
        <p class="facts-item">Organic Cordyceps<br>(Cordyceps Militaris)<br>fruitbody extract</p>
        <p class="facts-note">*Daily value not established</p>
      </div>
      <div class="panel-block">
        <h3>Other ingredients:</h3>
        <p>spring Water, Cane, Alcohol.<br>Alcohol content -20%</p>
      </div>
      <div class="panel-block">
        <h3>Suggested use:</h3>
        <p>Take two droppers full daily on the tongue or add to your favorite beverage</p>
      </div>
      <div class="panel-block">
        <h3>Storage:</h3>
        <p>Store in a cool, dry place away from sunlight.</p>
      </div>
    </section>

    <p class="disclaimer">These statements have not been evaluated by the BQC. This product is not intended to diagnose, treat, cure, or prevent any disease.</p>

    <div class="brand-dot" aria-hidden="true"></div>
    <h1 class="brand-name">Fernhollow</h1>
    <p class="product-name">CORDYCEPS</p>
    <div class="mini-shroom" style="left:271px" role="img" aria-label="Small red spotted mushroom"></div>
    <div class="mini-shroom" style="left:621px" role="img" aria-label="Small red spotted mushroom"></div>
    <p class="format-pill">LIQUID DROPS</p>
    <p class="volume">2 fl. oz / (60 ml)</p>

    <section class="panel benefits-panel">
      <h2 class="benefits-headline">Boost energy<br>and improve<br>endurance</h2>
      <h3 class="benefits-title">Key benefits:</h3>
      <ul class="benefits-list">
        <li>ENHANCES<br>ENERGY</li>
        <li>STAMINA</li>
        <li>OXYGEN<br>UTILIZATION</li>
      </ul>
      <div class="benefits-icon" role="img" aria-label="Small blue mushroom illustration"></div>
    </section>
  </main>
</body>
</html>
```